GOLD GUTSCHEIN
Zielgruppe
Zielgruppe sind Klienten ab 18 Jahren bis 60. Konzentration soll auf die Schicht zwischen 25 und 35 in der gehobenen Mittelschicht gelegt werden.
Im Vordergrund steht unser FlagShip Produkt ein Gold Ansparplan von der Firma ORU Infos auf www.quillbarrow.com
Es werden allerdings auch auch Vermögensberatung, Versicherungsberatung und Finanzierungsberatung zusätzlich angeboten.Produkt!
Aufgabenstellung
Gestaltungsvorlage für den Reisegutschein
in Form von einen Goldbarren

```html
<!DOCTYPE html>
<html lang="de">
<head>
<meta charset="utf-8">
<title>Reisegutschein Gold</title>
<link href="https://fonts.googleapis.com/css2?family=Oswald:wght@300;400&family=Open+Sans:wght@400;600&display=swap" rel="stylesheet">
<style>
:root{
  --page:#ffffff;
  --band:#2b2a28;
  --white:#ffffff;
  --ink:#1e1e1e;
  --gold-dark:#5a3c08;
  --gold-mid:#b98a2a;
  --gold-light:#f0cf78;
}
*{margin:0;padding:0;box-sizing:border-box}
html,body{width:1200px;height:1200px;overflow:hidden;background:var(--page)}
body{position:relative;font-family:"Open Sans",Arial,sans-serif;color:var(--white)}
.voucher{position:absolute;left:108px;width:982px;overflow:hidden}
.voucher--front{top:84px;height:482px}
.voucher--back{top:648px;height:480px}
.gold-photo{position:absolute;left:0;top:0;width:100%;height:100%;
  background:
   repeating-linear-gradient(112deg,rgba(70,40,0,.45) 0 6px,transparent 6px 150px),
   linear-gradient(160deg,var(--gold-dark) 0%,var(--gold-mid) 25%,var(--gold-light) 45%,var(--gold-mid) 62%,var(--gold-dark) 80%,var(--gold-mid) 100%)}
.band{position:absolute;left:0;width:100%;background:var(--band)}
.front-band{top:242px;height:180px}
.front-title{position:absolute;left:56px;top:20px;font-family:"Oswald",sans-serif;font-weight:300;font-size:74px;line-height:1;letter-spacing:.3px;white-space:nowrap}
.amount-words{position:absolute;left:476px;top:102px;font-size:7px;font-weight:600;white-space:nowrap}
.front-fields{position:absolute;left:58px;top:126px;width:396px;height:35px;background:var(--white);color:var(--ink);font-family:"Oswald",sans-serif;font-size:15px;font-weight:300;line-height:35px}
.front-fields span{position:absolute;top:0}
.field-nr{left:8px}.field-valid{left:182px}
.issuer-mark{position:absolute;left:778px;top:36px;width:144px;display:flex;align-items:center;justify-content:center;gap:8px;font-family:"Oswald",sans-serif;font-weight:400;font-size:26px;line-height:1;color:var(--gold-light)}
.issuer-mark i{display:block;width:20px;height:20px;background:var(--gold-light)}
.back-terms{top:44px;height:268px;padding:16px 58px 0}
.terms-title{font-size:12px;font-weight:400;margin-bottom:10px}
.terms-small{font-size:5.6px;line-height:1.55;margin-bottom:9px}
.terms-head{font-size:9.5px;font-weight:400;margin-bottom:3px}
.terms-body{font-size:9.5px;line-height:1.3;margin-bottom:9px;padding-right:40px}
.back-valid{position:absolute;right:60px;top:16px;width:173px;height:34px;background:var(--white);color:var(--ink);font-family:"Oswald",sans-serif;font-weight:300;font-size:15px;line-height:34px;padding-left:8px}
.back-contact{top:346px;height:93px}
.contact-col{position:absolute;top:16px;font-size:10.5px;line-height:1.3}
.contact-col h3{font-weight:400;font-size:13px;margin-bottom:10px}
.col-one{left:58px}.col-two{left:331px;top:38px}.col-three{left:604px}
</style>
</head>
<body>
<section class="voucher voucher--front">
  <div class="gold-photo" role="img" aria-label="Foto gestapelter Feingold-Barren, je 1 Kilo"></div>
  <div class="band front-band">
    <h1 class="front-title">Reisegutschein € 100,-</h1>
    <p class="amount-words">(Betrag in Worten: Euro einhundert)</p>
    <div class="front-fields"><span class="field-nr">Nr.</span><span class="field-valid">Gültig bis:</span></div>
    <p class="issuer-mark"><i></i>ORU</p>
  </div>
</section>

<section class="voucher voucher--back">
  <div class="gold-photo" role="img" aria-label="Foto gestapelter Feingold-Barren"></div>
  <div class="band back-terms">
    <div class="back-valid">Gültig bis:</div>
    <h2 class="terms-title">Reisegutschein</h2>
    <p class="terms-small">Dieser Reisegutschein ist einlösbar auf Buchungen von:</p>
    <p class="terms-head">Kurzurlaubspackages und Hotelangeboten der Velbrook Partnerhotels</p>
    <p class="terms-small">Ob Sommerurlaub, Winterurlaub, Wellnessurlaub oder Erlebnisurlaub – machen Sie Urlaub wie es Ihnen gefällt! Die aktuellen Angebote finden Sie im Internet auf www.velbrookreisen.at. Die max. Einlösehöhe ist beim jeweiligen Angebot beschrieben. Ebenso informiert Sie die Velbrook Kundenservice- und Reservierungszentrale über alle Angebote.</p>
    <p class="terms-body">Die Buchung und Einlösung der Kurzurlaubspackages und Hotelangebote ist ausschließlich über die Velbrook Kundenservice- und Reservierungszentrale möglich und kann nicht direkt im Hotel durchgeführt werden.</p>
    <p class="terms-head">Pauschalreise-Katalogangebote der gängigen Reiseveranstalter (ausgenommen Sonderangebote)</p>
    <p class="terms-small">Der Reisegutschein ist für alle Flugpauschalreisen und Kreuzfahrten aus Katalogen der gängigen Reiseveranstalter mit einer Reisedauer ab einer Woche unabhängig der Höhe des gebuchten Reisepreises einlösbar. Pro Reisebuchung kann nur ein Reisegutschein eingelöst werden. Die Einlösung des Reisegutscheines ist nicht mit anderen Marketing- und Promotionaktionen kombinierbar. Eine Anrechnung auf bereits bestehende Buchungen ist nicht möglich. Einzelleistungen wie nur Flug oder nur Hotel sind keine Pauschalreise-Katalogangebote.</p>
    <p class="terms-body">Die Buchung und Einlösung erfolgt telefonisch unter der nebenstehenden Buchungs-Hotline beim jeweils aktuellen Reisebüropartner der Velbrook Marketing GmbH.</p>
    <p class="terms-small">Die Buchung gemeinsam reisender Personen (Familie) gilt als eine Buchung, für die die marktübliche Buchungsgebühr verrechnet wird. Der Reisegutschein kann nicht in bar abgelöst werden. Die Einlösung erfolgt gemäß den Gültigkeitsbestimmungen auf www.velbrookreisen.at.</p>
    <p class="terms-small">Dieser Reisegutschein wurde als Incentive bzw. im Rahmen einer Marketingaktion von Firmenname einzeln als Geschenk ausgegeben und ist nur befristet zur Einlösung gültig. Der Reisegutschein darf vom Empfänger des Geschenks nicht weiterverkauft werden.</p>
  </div>
  <div class="band back-contact">
    <div class="contact-col col-one">
      <h3>Buchungs-Hotlines</h3>
      <p>Pauschalreise-Katalogangebote<br>+43/(0)7000/40 118 310<br>office@velbrookreisen.at</p>
    </div>
    <div class="contact-col col-two">
      <p>Kurzurlaubspackages und Hotelangebote<br>+43/(0)7000/40 118 302<br>office@velbrook-kurzurlaub.at</p>
    </div>
    <div class="contact-col col-three">
      <h3>Gutscheinaussteller:</h3>
      <p>Velbrook Marketing GmbH<br>Lindenhofgasse 14, A-4820 Talheim<br>FN 482915k, Firmenbuch LG Talheim</p>
    </div>
  </div>
</section>
</body>
</html>
```